依頼詳細
会社で使用する封筒(角2、長3の2サイズ)のデザインをお願いします。

【カラーリング】
・別添の弊社ロゴマークに使用してある色(特に濃青)や白を基調とした色

【デザイン】
・なるべくシンプルなもので、目を引くような

【用途】
(角2)お客様への提案資料用、新卒採用 等
(長3)請求書等の書類のやりとり

※両サイズともデザインを統一して頂ければと思います。
記載項目
会社名(株式会社 朝凪ソリューション)、ロゴマーク
希望イメージ
• +5 0 +5
• シンプル
複雑
• 単色
カラフル
• 暗い
明るい
• 日常
高級
• 遊び心
厳粛
• 未来的
伝統的
• 女性的
男性的
希望する色
青系
納品ファイル
• 高解像度JPG (.jpg)
補足説明
依頼公開後の追記内容
デザイナーの皆様、ご提案ありがとうございます。
デザインについて追記させて頂きます。

封筒へは、弊社所在地の記載は不要です。
(移転があった場合にデザインの変更や刷り直しをなくすため)

また、弊社ロゴマークに使われている濃いめの青をもう少し出して
頂けるとありがたいです。
(グラデーションで段々と濃い→薄いという感じが理想です)

色々と注文して申し訳ありませんが、ご対応よろしくお願いします。
■ 選んだ理由

現在、弊社では封筒をはじめ、名刺や会社案内などの印刷物のデザインを刷新しようとしており、これまでのイメージを変えるシンプルながら斬新なデザインに魅力を感じました。封筒や名刺、提案資料のテンプレートなど様々な用途を考えた際に、一番使いやすくしっくり来た点が選択した一番の理由となります。

■ 提案者全員のお礼・コメント

依頼した本人が、既製封筒への印刷なのかオーダーメイド封筒なのかを分かっていないまま依頼した事で、一部のデザイナー様にご迷惑をお掛けしたことをお詫びいたします。こんなにたくさんのご提案を頂き、正直選ぶのに大変苦労を致しました。本当にありがとうございました。

```html
<!DOCTYPE html>
<html lang="ja">
<head>
<meta charset="utf-8">
<title>株式会社 朝凪ソリューション 角2封筒</title>
<link rel="stylesheet" href="https://fonts.googleapis.com/css2?family=Oswald:wght@600&family=Noto+Sans+JP:wght@400;700&family=Roboto:wght@400;900&display=swap">
<style>
  :root {
    --backdrop: #e6e6e6;
    --paper: #ffffff;
    --paper-shade: #f1f1f1;
    --fold-line: #d6d6d6;
    --brand-blue: #1d4fa3;
    --ghost-gray: #e3e3e3;
    --ink: #333333;
    --ink-soft: #666666;
  }
  html, body {
    margin: 0;
    padding: 0;
    width: 849px;
    height: 1200px;
    overflow: hidden;
    background: var(--backdrop);
  }
  .canvas {
    position: relative;
    width: 849px;
    height: 1200px;
  }
  .envelope {
    position: absolute;
    left: 119px;
    top: 51px;
    width: 611px;
    height: 1067px;
    background: var(--paper);
    box-shadow: 0 4px 14px rgba(0,0,0,0.18);
  }
  .envelope__flap {
    position: absolute;
    left: 0;
    top: 0;
    width: 611px;
    height: 78px;
    background: linear-gradient(var(--paper), var(--paper-shade));
    border-bottom: 1px solid var(--fold-line);
  }
  .brand-mark {
    position: absolute;
    top: 26px;
    left: 0;
    width: 100%;
    text-align: center;
    font-family: "Roboto", sans-serif;
    font-weight: 900;
    font-size: 34px;
    letter-spacing: 1px;
    color: var(--brand-blue);
    line-height: 1;
  }
  .ghost-name {
    position: absolute;
    left: 18px;
    top: 172px;
    width: 620px;
    transform-origin: 0 0;
    transform: translate(62px, 0) rotate(90deg);
    font-family: "Oswald", sans-serif;
    font-weight: 600;
    font-size: 58px;
    line-height: 1;
    color: var(--ghost-gray);
    white-space: nowrap;
  }
  .sender-logo {
    position: absolute;
    left: 17px;
    top: 922px;
    font-family: "Roboto", sans-serif;
    color: var(--brand-blue);
  }
  .sender-logo__name {
    display: block;
    font-weight: 900;
    font-size: 54px;
    line-height: 1;
  }
  .sender-logo__tagline {
    display: block;
    margin-top: 3px;
    font-weight: 400;
    font-size: 9px;
    letter-spacing: 0.3px;
  }
  .sender-info {
    position: absolute;
    left: 198px;
    top: 855px;
    width: 400px;
    font-family: "Noto Sans JP", sans-serif;
    color: var(--ink);
  }
  .sender-info__company {
    font-weight: 700;
    font-size: 14px;
    margin: 0 0 8px;
    letter-spacing: 1px;
  }
  .office {
    display: flex;
    align-items: flex-start;
    margin-bottom: 8px;
  }
  .office__check {
    width: 10px;
    height: 10px;
    border: 1px solid var(--ink-soft);
    margin: 3px 6px 0 0;
    flex: none;
  }
  .office__label {
    font-weight: 700;
    font-size: 9px;
    width: 48px;
    flex: none;
    padding-top: 2px;
  }
  .office__detail {
    font-size: 8px;
    line-height: 1.55;
    color: var(--ink-soft);
  }
  .sender-info__web {
    font-size: 9px;
    margin-top: 4px;
  }
  .sender-info__web span {
    font-weight: 700;
    margin-right: 18px;
  }
</style>
</head>
<body>
<main class="canvas">
  <section class="envelope" aria-label="角2封筒 表面デザイン">
    <div class="envelope__flap">
      <div class="brand-mark">ASN</div>
    </div>

    <div class="ghost-name" aria-hidden="true">Asanagi Solution Center</div>

    <div class="sender-logo">
      <span class="sender-logo__name">ASN</span>
      <span class="sender-logo__tagline">Asanagi Solution</span>
    </div>

    <div class="sender-info">
      <p class="sender-info__company">株式会社 朝凪ソリューション</p>
      <div class="office">
        <span class="office__check"></span>
        <span class="office__label">東京本社</span>
        <span class="office__detail">〒100-0005 東京都千代田区丸の内2丁目4番1号（朝凪ビル6F）<br>TEL（03）5555-0101　FAX（03）5555-0102</span>
      </div>
      <div class="office">
        <span class="office__check"></span>
        <span class="office__label">広島本社</span>
        <span class="office__detail">〒730-0011 広島県広島市中区基町8番12号（朝凪ビル3F）<br>TEL（082）555-0201　FAX（082）555-0202</span>
      </div>
      <p class="sender-info__web"><span>ホームページ</span>http://www.asanagi-sol.example</p>
    </div>
  </section>
</main>
</body>
</html>
```